Criação de Folder para Logística, Entrega & Armazenamento
" Na grande maioria dos meus negocio, hoje estamos com foco na venda de Gesso Agrícola, Calcário e milho. fazemos negócios com Produtores rurais e granjas. vendemos o gesso e entregamos com a nossa frota de caminhões seja, frota própria ou caminhões agregado. da mesma maneira são os negócios com grãos, originamos os grãos dos produtores e vedemos para as granjas, entregamos com a nossa frota própria ou caminhões agregados. "

```html
<!DOCTYPE html>
<html lang="pt-BR">
<head>
<meta charset="UTF-8">
<title>Folder Terra Alta – Logística, Entrega e Armazenamento</title>
<link rel="stylesheet" href="https://fonts.googleapis.com/css2?family=Montserrat:wght@700;800&family=Open+Sans:wght@400;600;700&display=swap">
<style>
  :root {
    --bg: #e6e7e9;
    --paper: #ffffff;
    --orange: #d9822b;
    --orange-light: #f0a54a;
    --brown: #8a5526;
    --ink: #2f2f2f;
    --text: #6b6b6b;
    --fold: rgba(0,0,0,0.10);
  }
  * { margin: 0; padding: 0; box-sizing: border-box; }
  html, body { width: 1200px; height: 1200px; overflow: hidden; background: var(--bg); }
  body { font-family: "Open Sans", Arial, sans-serif; position: relative; }

  .spread {
    position: absolute; left: 50px; top: 210px;
    width: 1100px; height: 780px;
    display: flex;
    box-shadow: 0 10px 30px rgba(0,0,0,0.15);
  }
  .page {
    position: relative; width: 550px; height: 780px;
    background: var(--paper); overflow: hidden;
  }
  .page--left { box-shadow: inset -14px 0 18px -14px var(--fold); }
  .page--right { box-shadow: inset 14px 0 18px -14px var(--fold); }

  .top-band { position: absolute; left: 0; top: 0; width: 550px; height: 70px; }

  .tag {
    position: absolute;
    background: var(--orange);
    color: #fff;
    font-family: "Montserrat", Arial, sans-serif;
    font-weight: 800;
    font-size: 20px;
    line-height: 1.1;
    text-transform: uppercase;
    padding: 8px 12px;
  }
  .body-text {
    position: absolute;
    font-size: 12.5px;
    line-height: 1.55;
    color: var(--text);
  }
  .body-text p + p { margin-top: 12px; }

  .about-tag { left: 30px; top: 62px; width: 200px; }
  .about-text { left: 30px; top: 150px; width: 195px; }

  .kicker {
    position: absolute; left: 278px; top: 170px;
    color: var(--orange); font-weight: 700; font-size: 15px;
  }
  .lead {
    position: absolute; left: 278px; top: 202px; width: 240px;
    color: var(--ink); font-weight: 700; font-size: 17px; line-height: 1.35;
  }
  .lead .accent { color: var(--orange); }

  .vision-tag { left: 300px; top: 300px; width: 150px; }
  .vision-text { left: 278px; top: 375px; width: 225px; }

  .photo { position: absolute; display: block; }
  .wave { position: absolute; left: 0; bottom: 0; width: 550px; height: 260px; }

  .field-photo { left: 24px; top: 62px; width: 190px; height: 120px; }
  .mission-tag { left: 300px; top: 58px; width: 140px; }
  .mission-text { left: 300px; top: 135px; width: 215px; }
  .sack-photo { left: 318px; top: 245px; width: 210px; height: 125px; }
  .values-tag { left: 40px; top: 270px; width: 160px; }
  .values-text { left: 40px; top: 350px; width: 235px; }

  .brand {
    position: absolute; right: 34px; bottom: 30px;
    display: flex; align-items: center; gap: 8px;
    color: #fff; font-size: 16px; font-weight: 600;
  }
  .brand-mark { width: 12px; height: 12px; background: #fff; }
</style>
</head>
<body>
<main class="spread">

  <!-- Página esquerda -->
  <section class="page page--left">
    <svg class="top-band" viewBox="0 0 550 70" aria-hidden="true">
      <path d="M0 0 H550 V14 C400 22 200 30 0 52 Z" fill="var(--orange)"/>
      <path d="M0 0 H550 V6 C400 12 200 18 0 34 Z" fill="var(--brown)"/>
    </svg>

    <h2 class="tag about-tag">Sobre a<br>Terra Alta</h2>
    <div class="body-text about-text">
      <p>Atuamos na venda de gesso agrícola, calcário e milho, atendendo produtores rurais e granjas em toda a região com agilidade e confiança no campo.</p>
      <p>Originamos os grãos direto dos produtores e levamos até as granjas com entrega segura e pontual.</p>
    </div>

    <p class="kicker">Sobre nós</p>
    <p class="lead">Entregamos com frota própria e/ou <span class="accent">agregados</span></p>

    <h2 class="tag vision-tag">Nossa<br>Visão</h2>
    <p class="body-text vision-text">Ser referência regional em logística de insumos e grãos, unindo o produtor rural às granjas com eficiência.</p>

    <svg class="wave" viewBox="0 0 550 260" role="img" aria-label="Fotografia de grãos de milho e sementes em colher de madeira">
      <defs>
        <linearGradient id="grainFill" x1="0" y1="0" x2="1" y2="1">
          <stop offset="0" stop-color="#f1d9a8"/>
          <stop offset="0.5" stop-color="#c99a55"/>
          <stop offset="1" stop-color="#7a5630"/>
        </linearGradient>
      </defs>
      <path d="M0 70 C120 40 220 60 330 120 C380 150 420 210 440 260 H0 Z" fill="url(#grainFill)"/>
      <path d="M0 58 C160 20 360 40 550 10" fill="none" stroke="var(--orange)" stroke-width="5"/>
      <path d="M0 66 C160 30 360 50 550 22" fill="none" stroke="var(--brown)" stroke-width="2"/>
    </svg>
  </section>

  <!-- Página direita -->
  <section class="page page--right">
    <svg class="top-band" viewBox="0 0 550 70" aria-hidden="true">
      <path d="M0 0 H550 V40 C380 24 180 14 0 12 Z" fill="var(--orange)"/>
      <path d="M0 0 H550 V24 C380 12 180 6 0 4 Z" fill="var(--brown)"/>
    </svg>

    <svg class="photo field-photo" viewBox="0 0 190 120" role="img" aria-label="Fotografia de mãos segurando grãos sobre plantação ao pôr do sol">
      <defs>
        <linearGradient id="fieldFill" x1="0" y1="0" x2="0" y2="1">
          <stop offset="0" stop-color="#cfe0ea"/>
          <stop offset="0.55" stop-color="#e8dcb0"/>
          <stop offset="1" stop-color="#8fa86a"/>
        </linearGradient>
      </defs>
      <rect width="190" height="120" fill="url(#fieldFill)"/>
    </svg>

    <h2 class="tag mission-tag">Nossa<br>Missão</h2>
    <p class="body-text mission-text">Vender e entregar gesso, calcário e milho com frota própria ou agregada, garantindo qualidade do carregamento à descarga.</p>

    <svg class="photo sack-photo" viewBox="0 0 210 125" role="img" aria-label="Fotografia de saco de juta com grãos de soja">
      <defs>
        <radialGradient id="sackFill" cx="0.5" cy="0.55" r="0.6">
          <stop offset="0" stop-color="#e6c98d"/>
          <stop offset="0.7" stop-color="#c9a56a"/>
          <stop offset="1" stop-color="#ffffff"/>
        </radialGradient>
      </defs>
      <rect width="210" height="125" fill="url(#sackFill)"/>
    </svg>

    <h2 class="tag values-tag">Nossos<br>Valores</h2>
    <p class="body-text values-text">Compromisso com prazos, respeito ao produtor, segurança nas estradas e transparência em cada negociação realizada.</p>

    <svg class="wave" viewBox="0 0 550 260" role="img" aria-label="Fotografia de caminhões da frota em pátio ao pôr do sol">
      <defs>
        <linearGradient id="truckFill" x1="0" y1="0" x2="1" y2="1">
          <stop offset="0" stop-color="#f7b34c"/>
          <stop offset="0.45" stop-color="#d7762e"/>
          <stop offset="1" stop-color="#5a3a25"/>
        </linearGradient>
      </defs>
      <path d="M0 150 C140 110 330 20 550 0 V260 H0 Z" fill="url(#truckFill)"/>
      <path d="M0 140 C140 100 330 10 550 -10" fill="none" stroke="var(--orange)" stroke-width="5"/>
    </svg>

    <div class="brand"><span class="brand-mark"></span>Terra Alta</div>
  </section>

</main>
</body>
</html>
```